Visitenkarten-Design für Ferienhausvermietung
Zielgruppe
Vermietung eines Ferienhauses
Aufgabenstellung
Die Visitenkarte sollte edel und hochwertig wirken...
Es wäre mir wichtig, dass die Visitenkarte im Querformat erstellt wird.
Die Farben vom Logo lauten:
green: C = 43 M = 0 Y = 100 N = 16
brown: C = 39 M = 57 J = 87 N = 53
sky blue: C = 14 M = 6 J = 6 N = 0
Aber bitte nicht so viel in den Visitenkarten verwenden. Die Visitenkarten sollen eher neutral gehalten werden.
Die Schriften
font
Lindeneck : Satisfaction
Ferienhaus : Corbert Regular
Flyer-Design für Ferienhausvermietung Flyer-Design für Ferienhausvermietung"
Es soll ein Flyer im Format DIN A4 erstellt werden. Der beidseitig bedruckt wird und dann 6seitig gefaltet wird. Ich benötige für den Flyer: Beschreibung/Ausstattung des Ferienhauses Beschreibung der Lage Beschreibung der Umgebung Anfahrt/Lage/Kontakt
Logo-Design für Ferienhaus ´Sa Morta´auf Mallorca mit eigenem Tennisplatz und Pool Logo-Design für Ferienhaus ´Sa Morta´auf Mallorca mit eigenem Tennisplatz und Pool"
Sie können sich meine Finca auf der Website: Casitorvent anschauen. Ort: Costitx Name des Hauses: Finca Reblat (heißt nur auf der Website so). Der Name am Tor Haus: Finca Sa Morta. Ich mag es gerne klassisch
Logo-Design für ein Feriendorf an der Ostsee Logo-Design für ein Feriendorf an der Ostsee"
* Nicht zu bunt, nicht zu verspielt, möglichst klar und aufgeräumt * In 2D, keine Schattierungen, keine Fotos im Hintergrund o. ä.. * Das Logo muss in allen Medien gut darstellbar sein! * Es sollte modern wirken, dennoch fröhlich, warm und einladend * Der Strand-/Wasserbezug muss deutlich we..
Flyer-Design für Ferienhaus Flyer-Design für Ferienhaus"
Flyerdesign für Ferienhaus: Din-Lang 2x gefalzt (übliche Format), 3 Seiten vorne und hinten.  Es sollte nach Möglichkeit an unsere Webseite (www.ferienhaus-kormoran-tidewik.de) angepasst werden, druckfertig sein und per PDF auf unserer Webseite zum Downloaden integriert werden können. Meh..
Logo-Design für Ferienhaus Logo-Design für Ferienhaus"
Wir suchen ein Moderenes Design gern berücksichtig in Kombination mit dem Naturpark Velmtaler Höhen. Da das Ferienhaus sich dort befindet.

```html
<!DOCTYPE html>
<html lang="de">
<head>
<meta charset="utf-8">
<title>Ferienhaus Lindeneck – Visitenkarte</title>
<link rel="stylesheet" href="https://fonts.googleapis.com/css2?family=Barlow:wght@400&family=Satisfy&display=swap">
<style>
  :root {
    --paper: #ffffff;
    --frame: #3a2616;
    --brown-deep: #9c8572;
    --brown-mid: #d9cbbe;
    --ghost-grey: #cbcdd1;
    --ink: #111111;
    --house-tone: #d8cabd;
    --leaf-tone: #cfe3b0;
    --logo-brown: #4a2f1d;
  }
  * { margin: 0; padding: 0; box-sizing: border-box; }
  html, body {
    width: 1200px; height: 786px; overflow: hidden;
    background: var(--paper);
  }
  .business-card {
    position: absolute;
    left: 33px; top: 26px;
    width: 1137px; height: 734px;
    border: 4px solid var(--frame);
    border-radius: 26px;
    overflow: hidden;
    background: linear-gradient(90deg, var(--paper) 0%, var(--paper) 50%, var(--brown-mid) 78%, var(--brown-deep) 100%);
    font-family: "Barlow", sans-serif;
  }
  .house-illustration {
    position: absolute;
    left: 0; top: 345px;
    width: 790px; height: 385px;
    background:
      radial-gradient(ellipse at 8% 30%, var(--leaf-tone) 0%, rgba(207,227,176,0) 22%),
      radial-gradient(ellipse at 82% 30%, var(--leaf-tone) 0%, rgba(207,227,176,0) 20%),
      radial-gradient(ellipse at 45% 45%, var(--house-tone) 0%, rgba(216,202,189,0.55) 45%, rgba(255,255,255,0) 75%);
    opacity: 0.85;
  }
  .ghost-name {
    position: absolute;
    left: 405px; top: 40px;
    font-size: 140px; line-height: 1;
    color: var(--ghost-grey);
    font-weight: 400;
    letter-spacing: 1px;
  }
  .house-title {
    position: absolute;
    right: 70px; top: 108px;
    font-size: 42px; line-height: 1;
    color: var(--ink);
  }
  .brand-mark {
    position: absolute;
    left: 57px; top: 44px;
    width: 270px; height: 270px;
    display: flex; align-items: center; justify-content: center;
  }
  .brand-mark svg { position: absolute; inset: 0; }
  .brand-name {
    position: relative;
    font-size: 44px;
    color: var(--logo-brown);
  }
  .owner-name {
    position: absolute;
    left: 0; right: 150px; top: 360px;
    text-align: right;
    padding-right: 120px;
    font-family: "Satisfy", cursive;
    font-size: 104px; line-height: 1;
    color: var(--ink);
    text-shadow: 3px 4px 5px rgba(0,0,0,0.3);
  }
  .contact {
    position: absolute;
    font-size: 35px; line-height: 43px;
    color: var(--ink);
    text-shadow: 0 0 4px var(--paper), 0 0 2px var(--paper);
  }
  .contact-address { left: 72px; top: 561px; }
  .contact-online { right: 70px; top: 604px; text-align: right; }
</style>
</head>
<body>
  <div class="business-card">
    <div class="house-illustration" role="img" aria-label="Zarte Zeichnung des Ferienhauses mit Bäumen und Vögeln"></div>

    <div class="ghost-name" aria-hidden="true">Lindeneck</div>
    <div class="house-title">Ferienhaus Lindeneck</div>

    <div class="brand-mark">
      <svg width="270" height="270" viewBox="0 0 270 270" aria-hidden="true">
        <circle cx="135" cy="135" r="130" fill="none" stroke="var(--logo-brown)" stroke-width="5"/>
      </svg>
      <span class="brand-name">Lindeneck</span>
    </div>

    <div class="owner-name">Helga Marx</div>

    <div class="contact contact-address">
      Lindtal 12<br>
      91658 Bergenau<br>
      Tel: 09823/4718206
    </div>
    <div class="contact contact-online">
      info@lindeneck-ferienhaus.de<br>
      www.lindeneck-ferienhaus.de
    </div>
  </div>
</body>
</html>
```